KVR Biz Cards

We are a property management company that manages luxury level residential estates. As such, we need a business card design that gives a high end feel. The idea at the moment is to list the services offered on the back of the card, and our company information on the front of the card.

Services for the back of the card are as follows:
Professional Property Management service, Home Hosting & Concierge Service, Holiday Home / Rental Property Management

```html
<!DOCTYPE html>
<html lang="en">
<head>
<meta charset="utf-8">
<title>KVR Biz Cards</title>
<link href="https://fonts.googleapis.com/css2?family=Montserrat:wght@400;500;600;700&display=swap" rel="stylesheet">
<style>
  :root {
    --bronze: #8c5a24;
    --bronze-light: #a06a2e;
    --ink: #1d1d1d;
    --paper: #ffffff;
    --stage: #1e1e1e;
  }
  * { margin: 0; padding: 0; box-sizing: border-box; }
  html, body { width: 1200px; height: 852px; overflow: hidden; }
  body {
    background: var(--stage);
    font-family: "Montserrat", Arial, sans-serif;
    position: relative;
  }
  .card {
    position: absolute;
    width: 560px;
    height: 320px;
    overflow: hidden;
  }
  /* Back side */
  .card-back {
    left: 60px; top: 80px;
    background: var(--bronze);
    color: var(--paper);
    text-align: center;
  }
  .brand { display: flex; flex-direction: column; align-items: center; }
  .card-back .brand { margin-top: 56px; }
  .brand-mark { display: flex; align-items: center; gap: 10px; }
  .brand-square { width: 22px; height: 22px; }
  .brand-initials { font-weight: 600; font-size: 44px; letter-spacing: 2px; line-height: 1; }
  .brand-name { font-weight: 600; font-size: 20px; letter-spacing: 0.5px; margin-top: 10px; }
  .brand-tagline { font-weight: 500; font-size: 12.5px; margin-top: 2px; }
  .card-back .brand-square { background: var(--paper); }
  .services { margin: 30px auto 0; width: 480px; font-size: 12.5px; font-weight: 500; line-height: 1.7; }
  .services .rule { height: 1px; background: rgba(255,255,255,0.8); }
  .services p { margin: 6px 0; white-space: nowrap; }

  /* Front side */
  .card-front {
    left: 580px; top: 450px;
    background: var(--paper);
    color: var(--ink);
  }
  .card-front .brand { position: absolute; right: 40px; top: 30px; align-items: flex-end; }
  .card-front .brand-initials { color: var(--bronze); font-size: 38px; }
  .card-front .brand-square { background: var(--bronze); }
  .card-front .brand-name { color: var(--ink); font-size: 17px; }
  .card-front .brand-tagline { color: var(--bronze-light); font-size: 11px; }
  .rule-bronze { position: absolute; right: 40px; top: 150px; width: 250px; height: 2px; background: var(--bronze); }
  .address { position: absolute; right: 40px; top: 166px; text-align: right; font-size: 13px; line-height: 1.45; font-style: normal; }
  .edge-bar { position: absolute; left: 0; top: 186px; width: 10px; height: 30px; background: var(--bronze); }
  .person { position: absolute; left: 40px; top: 180px; }
  .person-name { color: var(--bronze); font-weight: 700; font-size: 22px; letter-spacing: 0.5px; }
  .person-role { font-size: 13px; letter-spacing: 1px; }
  .rule-ink { position: absolute; left: 40px; top: 234px; width: 250px; height: 1.5px; background: var(--ink); }
  .contacts { position: absolute; left: 40px; top: 244px; list-style: none; font-size: 13px; line-height: 1.45; }
  .contacts li { display: flex; align-items: center; gap: 8px; }
  .contacts svg { width: 11px; height: 11px; fill: none; stroke: var(--bronze); stroke-width: 1.6; }
</style>
</head>
<body>
  <section class="card card-back">
    <div class="brand">
      <div class="brand-mark"><span class="brand-square"></span><span class="brand-initials">KVR</span></div>
      <div class="brand-name">KAVERI MANAGEMENT</div>
      <div class="brand-tagline">Crafted to Keep Your Home at Ease</div>
    </div>
    <div class="services">
      <div class="rule"></div>
      <p>Luxury Estate Management | Guest Hosting &amp; Concierge Care<br>Holiday Home / Rental Property Management</p>
      <div class="rule"></div>
    </div>
  </section>

  <section class="card card-front">
    <div class="brand">
      <div class="brand-mark"><span class="brand-square"></span><span class="brand-initials">KVR</span></div>
      <div class="brand-name">KAVERI MANAGEMENT</div>
      <div class="brand-tagline">Crafted to Keep Your Home at Ease</div>
    </div>
    <div class="rule-bronze"></div>
    <address class="address">Calle Marina 42,<br>Port Verde, 07990,<br>Mallorca, Spain</address>
    <div class="edge-bar"></div>
    <div class="person">
      <div class="person-name">DANIEL REYES</div>
      <div class="person-role">DIRECTOR</div>
    </div>
    <div class="rule-ink"></div>
    <ul class="contacts">
      <li><svg viewBox="0 0 12 12"><path d="M2 1.5l2 .5 1 2.5-1.3 1a6 6 0 0 0 2.8 2.8l1-1.3 2.5 1 .5 2c-5 1-9.5-3.5-8.5-8.5z"/></svg>+34-971-555-026</li>
      <li><svg viewBox="0 0 12 12"><rect x="1" y="2.5" width="10" height="7"/><path d="M1 2.5l5 4 5-4"/></svg>hello@kavericare.com</li>
      <li><svg viewBox="0 0 12 12"><circle cx="6" cy="6" r="5"/><path d="M1 6h10M6 1c-2.5 3-2.5 7 0 10M6 1c2.5 3 2.5 7 0 10"/></svg>www.kavericare.com</li>
    </ul>
  </section>
</body>
</html>
```